Harbor Relay Group Letterhead Design

The project name sums it up. Just need a professional letterhead design / template we can use in our marketing folders.

Here's the address / contact info for the letterhead: Harbor Relay Group 4815 Maple Crest Ave Suite 210 League City, Texas 77419 346-507-3846 www.harborrelaygroup.us support@harborrelaygroup.us

```html
<!DOCTYPE html>
<html lang="en">
<head>
<meta charset="utf-8">
<title>Harbor Relay Group Letterhead</title>
<link href="https://fonts.googleapis.com/css2?family=Montserrat:wght@400;500;700;800&display=swap" rel="stylesheet">
<style>
  :root {
    --backdrop: #e6e7e9;
    --paper: #ffffff;
    --brand-blue: #1f55b0;
    --ink: #1c1c1c;
    --ink-soft: #3a3a3a;
    --rule-grey: #8a8a8a;
    --band-black: #0b0b0b;
  }
  * { box-sizing: border-box; margin: 0; padding: 0; }
  html, body {
    width: 1200px; height: 874px; overflow: hidden;
    background: var(--backdrop);
    font-family: "Montserrat", sans-serif;
  }
  .letterhead {
    position: absolute; left: 300px; top: 13px;
    width: 600px; height: 848px;
    background: var(--paper);
    box-shadow: 0 6px 22px rgba(0,0,0,.12);
    color: var(--ink);
  }
  .brand {
    position: absolute; left: 48px; top: 52px;
    display: flex; align-items: center; gap: 10px;
  }
  .brand-square {
    width: 34px; height: 34px; background: var(--brand-blue); flex: none;
  }
  .brand-name {
    font-weight: 800; font-size: 16px; color: var(--brand-blue);
    letter-spacing: .3px; text-transform: uppercase; white-space: nowrap;
  }
  .header-divider {
    position: absolute; left: 342px; top: 40px;
    width: 1px; height: 66px; background: var(--rule-grey);
  }
  .contact {
    position: absolute; left: 356px; top: 38px;
    font-size: 9px; line-height: 13px; color: var(--ink-soft);
    font-style: normal; white-space: nowrap;
  }
  .contact-line { display: flex; align-items: center; gap: 5px; }
  .contact-line svg { width: 8px; height: 8px; fill: var(--brand-blue); }
  .header-rule {
    position: absolute; left: 48px; right: 34px; top: 118px;
    height: 2px; background: var(--brand-blue);
  }
  .recipient {
    position: absolute; left: 70px; top: 168px;
    font-size: 10px; line-height: 14px;
  }
  .letter-body {
    position: absolute; left: 70px; top: 238px; width: 470px;
    font-size: 10px; line-height: 15px; color: var(--ink);
  }
  .letter-body p { margin-bottom: 15px; }
  .closing { margin-top: 6px; }
  .signature-area {
    margin-top: 10px; width: 120px; height: 40px;
    background: linear-gradient(90deg, #efefef, #f8f8f8);
  }
  .footer-bands {
    position: absolute; left: 0; bottom: 26px; width: 600px; height: 60px;
  }
  .footer-url {
    position: absolute; left: 402px; bottom: 66px;
    display: flex; align-items: center; gap: 6px; white-space: nowrap;
    font-size: 10px; color: #fff; font-weight: 500;
  }
  .footer-url svg { width: 9px; height: 9px; fill: #fff; }
</style>
</head>
<body>
<main class="letterhead">
  <header>
    <div class="brand">
      <span class="brand-square"></span>
      <span class="brand-name">Harbor Relay Group</span>
    </div>
    <div class="header-divider"></div>
    <address class="contact">
      <div>4815 Maple Crest Ave</div>
      <div>Suite 210 League City,</div>
      <div>Texas 77419</div>
      <div class="contact-line">
        <svg viewBox="0 0 10 10"><path d="M2 0.5l2 2-1 1.2c.6 1.3 1.6 2.3 2.9 2.9l1.2-1 2 2-1.3 1.9C4.5 9.2 .8 5.5.3 1.8z"/></svg>
        346-507-3846
      </div>
      <div class="contact-line">
        <svg viewBox="0 0 10 10"><path d="M0 2h10v6H0z M0 2l5 3.5L10 2" /></svg>
        support@harborrelaygroup.us
      </div>
    </address>
    <div class="header-rule"></div>
  </header>

  <section class="recipient">
    <div>Mr/s</div>
    <div>First Name and Last Name</div>
    <div>Company Name</div>
    <div>Address</div>
  </section>

  <section class="letter-body">
    <p>Lorem Ipsum is simply dummy text of the printing and typesetting industry. Lorem Ipsum has been the industry's standard dummy text ever since the 1500s, when an unknown printer took a galley of type and scrambled it to make a type specimen book. It has survived not only five centuries, but also the leap into electronic typesetting, remaining essentially unchanged. It was popularised in the 1960s.</p>
    <p>The standard chunk of Lorem Ipsum used since the 1500s is reproduced below for those interested. Sections 1.10.32 and 1.10.33 from "de Finibus Bonorum et Malorum" by Cicero are also reproduced in their exact original form, accompanied by English versions from the 1914 translation by H. Rackham. Lorem ipsum dolor sit amet, consectetur adipiscing elit, sed do eiusmod tempor incididunt ut labore et dolore magna aliqua.</p>
    <p>It is a long established fact that a reader will be distracted by the readable content of a page when looking at its layout. The point of using Lorem Ipsum is that it has a more-or-less normal distribution of letters, as opposed to using 'Content here, content here', making it look like readable English. Many desktop publishing packages and web page editors now.</p>
    <div class="closing">Your Sincerely,</div>
    <div class="signature-area" role="img" aria-label="Handwritten signature"></div>
  </section>

  <footer>
    <svg class="footer-bands" viewBox="0 0 600 60" preserveAspectRatio="none">
      <polygon points="0,36 380,36 366,60 0,60" fill="var(--band-black)"/>
      <polygon points="392,0 572,0 558,28 378,28" fill="var(--brand-blue)"/>
      <polygon points="586,0 600,0 600,28 572,28" fill="var(--band-black)"/>
    </svg>
    <div class="footer-url">
      <svg viewBox="0 0 10 10"><circle cx="5" cy="5" r="5"/></svg>
      www.harborrelaygroup.us
    </div>
  </footer>
</main>
</body>
</html>
```